Marnie Vale Photography needs a unique, creative business card/logo design

I need a design for business cards/logo that is unique and creative in the industry. Simplicity is nice, so not too crowded. Something that will catch my customer's eye and remain in their memory. I am primarily a landscape photographer but will be soon may be branching into boudoir photography as well. I have attached my current card.

Marnie Vale Photography
Phone: 0439 517 264
Email: MarnieValePhotography@quillmail.example
Website: www.snapnook.example/MarnieValePhotography.Aust

Marnie Vale Photography

• Contact Details on one side
• pixelation

```html
<!DOCTYPE html>
<html lang="en">
<head>
<meta charset="utf-8">
<title>Marnie Vale Photography – Business Card</title>
<link rel="stylesheet" href="https://fonts.googleapis.com/css2?family=Crimson+Text:wght@400&display=swap">
<style>
  :root {
    --backdrop: #ececec;
    --card: #ffffff;
    --ink: #4a4a4a;
    --ink-soft: #6b6b6b;
    --rule: #5a5a5a;
    --shadow: rgba(0, 0, 0, 0.12);
  }
  * { box-sizing: border-box; margin: 0; padding: 0; }
  html, body {
    width: 1200px;
    height: 800px;
    overflow: hidden;
  }
  body {
    background: var(--backdrop);
    font-family: "Crimson Text", Georgia, serif;
    color: var(--ink);
    display: flex;
    align-items: center;
    justify-content: center;
    gap: 60px;
  }
  .card {
    width: 490px;
    height: 280px;
    background: var(--card);
    box-shadow: 0 10px 30px var(--shadow);
    position: relative;
  }

  /* Contact side */
  .card--contact .rule {
    position: absolute;
    left: 0;
    right: 0;
    height: 1px;
    background: var(--rule);
  }
  .card--contact .rule--top { top: 30px; }
  .card--contact .rule--bottom { bottom: 30px; }
  .contact {
    position: absolute;
    inset: 31px 0;
    display: flex;
    flex-direction: column;
    align-items: center;
    justify-content: center;
    text-align: center;
    gap: 4px;
  }
  .contact__name {
    font-size: 15px;
    color: var(--ink-soft);
    letter-spacing: 0.02em;
  }
  .contact__phone {
    font-size: 22px;
    letter-spacing: 0.08em;
    color: var(--ink);
    margin-bottom: 4px;
  }
  .contact__line {
    font-size: 14px;
    color: var(--ink-soft);
    letter-spacing: 0.02em;
  }

  /* Brand side */
  .card--brand {
    display: flex;
    align-items: center;
    justify-content: center;
  }
  .brand {
    display: flex;
    align-items: center;
    gap: 12px;
  }
  .brand__mark {
    width: 14px;
    height: 14px;
    border: 1.5px solid var(--ink);
    border-radius: 50%;
    flex: none;
  }
  .brand__name {
    font-size: 20px;
    line-height: 1;
    letter-spacing: 0.08em;
    text-transform: uppercase;
    color: var(--ink);
    white-space: nowrap;
  }
</style>
</head>
<body>
  <section class="card card--contact" aria-label="Contact side">
    <div class="rule rule--top"></div>
    <div class="contact">
      <p class="contact__name">Marnie Vale Photography</p>
      <p class="contact__phone">0439 517 264</p>
      <p class="contact__line">MarnieValePhotography@quillmail.example</p>
      <p class="contact__line">www.snapnook.example/MarnieValePhotography.Aust</p>
    </div>
    <div class="rule rule--bottom"></div>
  </section>

  <section class="card card--brand" aria-label="Brand side">
    <div class="brand">
      <span class="brand__mark" aria-hidden="true"></span>
      <p class="brand__name">Marnie Vale Photography</p>
    </div>
  </section>
</body>
</html>
```